we can communicate on this, but i want to follow the approach we took on Pell|Quorn & Tillet but i feel the card front needs the black background and the platinum and gold logo. The back? I am open. we can use the same info from PQ&T. Vellum Crest is an enhanced equity investment fund - basically a very exclusive boutique hedge fund that uses only stock options. very advanced things. hope you are interested

Contact Information for Business Card

Dr. Owen T. Brisket, CFA
Scientifique de fusée financière
555.014.2296
TheDoc4793@mailvessel.example

4718 Fennel Brook Way N.
West Fargo, ND 58078

No web site

Colors

Designer to choose colors to be used in the design.

Requirements
Nice to have
• I tend to prefer the most visible applications of the logo to include logo and name, the logo version with a black background and the gold and platinum components separated by the black. I see this working well for a single side (logo and name - this is card front to me).
• I am fairly open to other treatments on the reverse side with the data. To me, it makes sense to have a different color rendition of the logo on the reverse and it may be a muted black tone on tone or an oversized portion that would have spot UV. Or, the reverse may play with colors and layout
Should not have
• Other colors = no no
• Decorative font

```html
<!DOCTYPE html>
<html lang="en">
<head>
<meta charset="utf-8">
<title>Vellum Crest — Business Card</title>
<link href="https://fonts.googleapis.com/css2?family=Montserrat:wght@400;600;700&family=Arimo:wght@400;700&display=swap" rel="stylesheet">
<style>
  :root {
    --stage: #1c1c1f;
    --card-black: #050505;
    --card-white: #ffffff;
    --gold: #c9a233;
    --ink: #111111;
    --muted: #2a2a2a;
    --faint: #f4f1e8;
  }
  * { margin: 0; padding: 0; box-sizing: border-box; }
  html, body { width: 1200px; height: 800px; overflow: hidden; }
  body { background: var(--stage); position: relative; font-family: "Arimo", Arial, sans-serif; }

  .card { position: absolute; width: 540px; height: 310px; overflow: hidden; box-shadow: 0 14px 34px rgba(0,0,0,.55); }

  /* Front */
  .card-front { left: 50px; top: 80px; background: var(--card-black); display: flex; align-items: center; justify-content: center; }
  .brand { display: flex; align-items: center; gap: 18px; }
  .brand-dot { width: 62px; height: 62px; border-radius: 50%; background: var(--gold); flex: none; }
  .brand-name { font-family: "Montserrat", Arial, sans-serif; font-weight: 700; font-size: 38px; line-height: 1; letter-spacing: 1px; text-transform: uppercase; white-space: nowrap; }
  .card-front .brand-name { color: #ffffff; }

  /* Back */
  .card-back { left: 610px; top: 410px; background: var(--card-white); color: var(--ink); }
  .back-accent { position: absolute; right: -40px; top: -70px; width: 270px; height: 270px; border-radius: 50%; background: var(--faint); }
  .holder { position: absolute; right: 24px; top: 24px; text-align: right; }
  .holder-name { font-weight: 700; font-size: 18px; text-transform: uppercase; letter-spacing: .3px; white-space: nowrap; }
  .holder-role { font-size: 12.5px; color: var(--gold); margin-top: 3px; white-space: nowrap; }

  .card-back .brand { position: absolute; left: 34px; top: 90px; gap: 14px; }
  .card-back .brand-dot { width: 52px; height: 52px; }
  .card-back .brand-name { color: var(--ink); font-size: 28px; }

  .address { position: absolute; right: 24px; top: 152px; text-align: right; font-size: 12.5px; line-height: 1.35; color: var(--muted); white-space: nowrap; }

  .divider { position: absolute; left: 34px; right: 22px; top: 192px; height: 1.5px; background: var(--ink); }

  .contacts { position: absolute; left: 34px; top: 210px; list-style: none; font-size: 13px; color: var(--muted); }
  .contacts li { display: flex; align-items: center; gap: 8px; height: 24px; white-space: nowrap; }
  .contact-icon { width: 15px; height: 15px; flex: none; }
</style>
</head>
<body>

  <section class="card card-front" aria-label="Card front">
    <div class="brand">
      <span class="brand-dot" aria-hidden="true"></span>
      <span class="brand-name">Vellum Crest</span>
    </div>
  </section>

  <section class="card card-back" aria-label="Card back">
    <div class="back-accent" aria-hidden="true"></div>

    <div class="holder">
      <div class="holder-name">Dr. Owen T. Brisket, CFA</div>
      <div class="holder-role">Scientifique de fusée financière</div>
    </div>

    <div class="brand">
      <span class="brand-dot" aria-hidden="true"></span>
      <span class="brand-name">Vellum Crest</span>
    </div>

    <div class="address">4718 Fennel Brook Way N.<br>West Fargo, ND 58078</div>

    <div class="divider"></div>

    <ul class="contacts">
      <li>
        <svg class="contact-icon" viewBox="0 0 16 16" aria-hidden="true"><circle cx="8" cy="8" r="8" fill="var(--gold)"/><path d="M5 4.5l1.6-.4.9 2-1 .8a5 5 0 0 0 2.6 2.6l.8-1 2 .9-.4 1.6c-3.6.3-6.8-2.9-6.5-6.5z" fill="#fff"/></svg>
        555.014.2296
      </li>
      <li>
        <svg class="contact-icon" viewBox="0 0 16 16" aria-hidden="true"><circle cx="8" cy="8" r="8" fill="var(--gold)"/><rect x="4" y="5" width="8" height="6" fill="#fff"/><path d="M4 5l4 3.2L12 5" fill="none" stroke="var(--gold)" stroke-width="1"/></svg>
        TheDoc4793@mailvessel.example
      </li>
    </ul>
  </section>

</body>
</html>
```